Business Card Design Project

Corwen Property Management

Our Business is residential property management, we therefore need a card that displays a professional image, but is clear and concise, and easy to read
Updates

We are committed now guys and girls, loving what we are seeing so far! 

Target Market(s)

Landlords, Rental Property Owners

Industry/Entity Type

Residential

Requirements
Must have
• Dean Fosterly - Principal
Tessa Fosterly - Director (Property Management)

PO Box 718
Holloway SA 5093

Dean: 0419 372 508
Tessa: 0419 613 947

www.corwenpropertymanagement.com.au
admin@corwenpropertymanagement.com.au

Nice to have
• I would like the card to be double sided, white background on the information side and then colour on the reverse, in blue or black and incorporating our logo

```html
<!DOCTYPE html>
<html lang="en">
<head>
<meta charset="utf-8">
<title>Corwen Property Management – Business Card</title>
<link rel="stylesheet" href="https://fonts.googleapis.com/css2?family=Roboto+Condensed:wght@400;700&display=swap">
<style>
  :root {
    --page: #5a5a5a;
    --card-black: #0b0b0c;
    --card-black-soft: #1c1d1f;
    --card-white: #ffffff;
    --wash: #e9edf3;
    --brand-blue: #1b7fc9;
    --name-blue: #2a8fd6;
    --ink-white: #f2f2f2;
    --ink-grey: #5c5c5c;
    --shadow: rgba(0, 0, 0, 0.45);
  }
  * { box-sizing: border-box; margin: 0; padding: 0; }
  html, body { width: 1200px; height: 900px; overflow: hidden; }
  body {
    background: var(--page);
    font-family: "Roboto Condensed", "Arial Narrow", sans-serif;
    display: flex;
    flex-direction: column;
    align-items: center;
    justify-content: center;
    gap: 48px;
  }
  .card {
    width: 640px;
    height: 366px;
    position: relative;
    overflow: hidden;
    box-shadow: 0 18px 40px var(--shadow);
  }

  /* Reverse side */
  .card--reverse { background: var(--card-black); }
  .card--reverse .texture {
    position: absolute; inset: 0;
    background: radial-gradient(ellipse at 40% 40%, var(--card-black-soft), var(--card-black) 75%);
  }
  .card--reverse .brand {
    position: absolute;
    left: 0; right: 0; top: 118px;
    display: flex; align-items: center; justify-content: center; gap: 16px;
  }
  .brand-mark { width: 54px; height: 54px; background: var(--brand-blue); flex: none; }
  .brand-name {
    font-weight: 700;
    line-height: 1;
  }
  .brand-name .line-main { display: block; font-size: 64px; letter-spacing: -1px; }
  .brand-name .line-sub { display: block; font-size: 20px; margin-top: 2px; }
  .card--reverse .brand-name { color: var(--ink-white); }
  .card--reverse .website {
    position: absolute; left: 0; right: 0; top: 262px;
    text-align: center;
    color: var(--name-blue);
    font-size: 15px;
    letter-spacing: 1.5px;
  }

  /* Information side */
  .card--info { background: var(--card-white); }
  .card--info .wash {
    position: absolute; left: 0; right: 0; top: 0; height: 190px;
    background: linear-gradient(90deg, var(--card-white) 30%, var(--wash) 100%);
  }
  .card--info .brand {
    position: absolute; left: 40px; top: 56px;
    display: flex; align-items: center; gap: 14px;
  }
  .card--info .brand-name { color: var(--ink-grey); }
  .card--info .details {
    position: absolute; left: 0; right: 0; bottom: 0; height: 176px;
    background: var(--card-black);
    color: var(--ink-white);
    display: grid;
    grid-template-columns: 1fr 1.45fr;
    padding: 30px 40px 0 40px;
    font-size: 15px;
    line-height: 1.65;
  }
  .person-name { color: var(--name-blue); font-size: 19px; }
  .person-role { font-size: 13px; margin-left: 6px; }
  .label { color: var(--name-blue); margin-right: 4px; }
</style>
</head>
<body>

  <section class="card card--reverse" aria-label="Card reverse">
    <div class="texture" role="img" aria-label="Dark tiled texture background"></div>
    <div class="brand">
      <span class="brand-mark"></span>
      <span class="brand-name"><span class="line-main">Corwen</span><span class="line-sub">Property Management</span></span>
    </div>
    <p class="website">www.corwenpropertymanagement.com.au</p>
  </section>

  <section class="card card--info" aria-label="Card information side">
    <div class="wash"></div>
    <div class="brand">
      <span class="brand-mark"></span>
      <span class="brand-name"><span class="line-main">Corwen</span><span class="line-sub">Property Management</span></span>
    </div>
    <div class="details">
      <div class="contact contact--principal">
        <p><span class="person-name">Dean Fosterly</span><span class="person-role">Principal</span></p>
        <p><span class="label">p:</span>0419 372 508</p>
        <p>PO Box 718</p>
        <p>Holloway SA 5093</p>
      </div>
      <div class="contact contact--director">
        <p><span class="person-name">Tessa Fosterly</span><span class="person-role">Director (Property Management)</span></p>
        <p><span class="label">p:</span>0419 613 947</p>
        <p><span class="label">e:</span>admin@corwenpropertymanagement.com.au</p>
        <p><span class="label">w:</span>www.corwenpropertymanagement.com.au</p>
      </div>
    </div>
  </section>

</body>
</html>
```